We are the world's leading center for transgender surgery and have multiple locations.

We want a unique and dynamic business card that wows potential patients and referral sources (physicians, previous patients, etc). We are open to inventive designs, card shape, additional design on the back of the card, etc.

We are a surgical practice in a competitive environment and want to stand out as the leader in transgender surgery. We have multiple surgeons with unique talents who are impeccably trained with extensive experience. We are dedicated to our patients and their needs. We want the card to stand out and impress them. We want it to be suitable to all of the surgeons as well as our staff.

Our practice started as a small practice in San Francisco, CA and now has an additional location in Austin Texas (as well as another city to be announced later). Our practice has plastic surgeons, reconstructive urologists, general surgeons and gynecologists.

We continue to boast some of the lowest published phalloplasty complication rates in the world and our San Francisco microsurgeons that we have been working with for more than a year and a half have 0 microvascular take backs and 0 flap failures. Between our two centers in San Francisco, California and Austin, Texas, we perform 5-6 phalloplasties per week, making us one of the largest volume centers in the world.

Target Market(s)

Potential Transgender patients (all genders) and referring physicians

Industry/Entity Type

Surgeon

Contact Information for Business Card

Here is an example of one of our physicians:

Daniel R. Ostrow, MD
Reconstructive Urology for the Transgender Community
Diplomate, National Council of Renal Medicine with subspecialty certification in FPS and Reconstructive Surgery

318 Lady Harriet Moore Ave
Suite 7
Larkfield, CA 94817

phone 415-738-1942
fax 415-582-1947

Font styles to use
Sans Serif

Requirements
Must have
• Must have a unique look, but tasteful.
Nice to have
• ?
Should not have
• ?

```html
<!DOCTYPE html>
<html lang="en">
<head>
<meta charset="utf-8">
<title>Lumen Center – Business Card</title>
<link rel="stylesheet" href="https://fonts.googleapis.com/css2?family=Saira:wght@400;500;700;800&display=swap">
<style>
  :root {
    --backdrop: #2a2c30;
    --card-white: #ffffff;
    --magenta: #c4206f;
    --navy: #1b2f78;
    --violet: #6a2a8c;
    --back-start: #c21d79;
    --back-mid: #7d2a93;
    --back-end: #243a92;
    --text-blue: #23386e;
  }
  * { box-sizing: border-box; margin: 0; padding: 0; }
  html, body { width: 1200px; height: 900px; overflow: hidden; }
  body {
    background: var(--backdrop);
    font-family: "Saira", sans-serif;
    position: relative;
  }
  .card {
    position: absolute;
    width: 540px;
    height: 308px;
    border-radius: 22px;
    overflow: hidden;
    box-shadow: 0 10px 30px rgba(0,0,0,0.35);
  }

  /* Front */
  .card-front { left: 70px; top: 470px; background: var(--card-white); }
  .front-brand {
    position: absolute; left: 30px; top: 22px;
    display: flex; align-items: center; gap: 12px;
  }
  .brand-dot { width: 44px; height: 44px; border-radius: 50%; background: var(--magenta); flex: none; }
  .brand-name {
    font-weight: 800; font-size: 34px; line-height: 1; letter-spacing: 0.5px;
    color: var(--navy); text-transform: uppercase; white-space: nowrap;
  }
  .brand-tagline {
    font-weight: 700; font-size: 9.5px; letter-spacing: 0.6px;
    color: var(--magenta); text-transform: uppercase; text-align: right; margin-top: 2px;
  }
  .front-details {
    position: absolute; right: 34px; top: 86px; width: 400px;
    text-align: right; color: var(--text-blue);
  }
  .person-name { font-weight: 500; font-size: 24px; color: var(--magenta); line-height: 1.1; }
  .name-rule {
    height: 2px; width: 210px; margin: 8px 0 8px auto;
    background: linear-gradient(90deg, var(--violet), var(--navy));
  }
  .credentials { font-size: 11.5px; line-height: 1.35; }
  .contact { font-size: 11.5px; line-height: 1.4; margin-top: 4px; }
  .contact .label { color: var(--magenta); }
  .stripe { position: absolute; left: 0; right: 0; height: 18px; }
  .stripe-magenta { top: 236px; background: var(--magenta); }
  .stripe-navy { top: 264px; background: var(--navy); }

  /* Back */
  .card-back {
    left: 590px; top: 130px;
    background: linear-gradient(135deg, var(--back-start) 0%, var(--back-mid) 50%, var(--back-end) 100%);
  }
  .back-texture {
    position: absolute; inset: 0;
    background: radial-gradient(circle at 30% 30%, rgba(255,255,255,0.08), transparent 60%);
  }
  .back-brand {
    position: absolute; left: 60px; top: 92px;
    display: flex; align-items: center; gap: 16px;
  }
  .back-brand .brand-dot { width: 62px; height: 62px; background: #ffffff; }
  .back-brand .brand-name { color: #ffffff; font-size: 46px; }
  .back-brand .brand-tagline { color: #ffffff; font-size: 11px; }
  .back-address {
    position: absolute; left: 60px; bottom: 52px;
    color: rgba(255,255,255,0.85); font-size: 13px; letter-spacing: 0.2px;
  }
</style>
</head>
<body>
  <section class="card card-back" aria-label="Card back">
    <div class="back-texture" role="img" aria-label="Soft magenta to blue gradient background"></div>
    <div class="back-brand">
      <div class="brand-dot"></div>
      <div>
        <div class="brand-name">Lumen Center</div>
        <div class="brand-tagline">For Transgender Surgery</div>
      </div>
    </div>
    <p class="back-address">318 Lady Harriet Moore Ave, Suite 7, Larkfield, CA 94817</p>
  </section>

  <section class="card card-front" aria-label="Card front">
    <div class="front-brand">
      <div class="brand-dot"></div>
      <div>
        <div class="brand-name">Lumen Center</div>
        <div class="brand-tagline">For Transgender Surgery</div>
      </div>
    </div>
    <div class="front-details">
      <h1 class="person-name">Daniel R. Ostrow, MD</h1>
      <div class="name-rule"></div>
      <p class="credentials">
        Reconstructive Urology for the Transgender Community<br>
        Diplomate, National Council of Renal Medicine with<br>
        subspecialty certification in FPS and Reconstructive Surgery
      </p>
      <p class="contact">
        <span class="label">Phone:</span> 415-738-1942 | <span class="label">Fax:</span> 415-582-1947<br>
        care@lumencenter.com | www.LumenCenter.com
      </p>
    </div>
    <div class="stripe stripe-magenta"></div>
    <div class="stripe stripe-navy"></div>
  </section>
</body>
</html>
```